Website redesign www.tidecrestpc.com law firm site

Need to redesign the website that I currently have to look more modern and professional. Would also like to be able to make updates and post without having a huge hassle. See current www.tidecrestpc.com. I just think that it looks very immature and it's very templated there's no ability for me to make posts or Add links or anything like that

Target Market(s)

California people looking for a powerhouse attorney in

Industry/Entity Type

Legal

Number of Pages Required

3 page

Font styles to use
Serif
Sans Serif

Colors
ec1f27
000000
ffffff

Requirements
Must have
• Must be mobile friendly. Must look professional and have ability to post links to other websites. Must have ability to post blogs or articles. Would like to be able to read my TallyDock account and also have the ability to upload forms for people to download
Nice to have
• Simple design easy to use and not cluttered with too much text

```html
<!DOCTYPE html>
<html lang="en">
<head>
<meta charset="utf-8">
<title>Tidecrest Law, P.C.</title>
<link href="https://fonts.googleapis.com/css2?family=Libre+Baskerville&family=Open+Sans:ital,wght@0,400;0,600;1,400&display=swap" rel="stylesheet">
<style>
:root{
  --red:#ec1f27;
  --black:#000;
  --white:#fff;
  --ink:#1a1a1a;
  --muted:#9a9a9a;
  --light:#ececec;
  --dark:#141414;
}
*{box-sizing:border-box;margin:0;padding:0}
html,body{width:1200px;height:3557px;overflow:hidden}
body{font-family:"Open Sans",Arial,sans-serif;color:var(--ink);background:var(--white)}
.section{position:relative;width:1200px;overflow:hidden}
.wrap{position:relative;width:1044px;margin:0 auto;height:100%}
h2{font-weight:400;font-size:40px;letter-spacing:.5px;text-align:center}
h2 .accent{color:var(--red)}
.btn{display:inline-block;background:var(--red);color:var(--white);font-size:19px;text-transform:uppercase;text-align:center;border-radius:4px}

/* header */
.header{height:110px}
.logo{position:absolute;left:78px;top:20px;width:270px;text-align:center;font-family:"Libre Baskerville",Georgia,serif;color:var(--red)}
.logo .name{font-size:38px;line-height:44px}
.logo .sub{font-size:15px;border-top:2px solid var(--red);margin-top:2px;padding-top:1px;position:relative}
.nav{position:absolute;left:368px;top:33px;display:flex;gap:0;list-style:none}
.nav li{font-size:16px;padding:0 11px;height:46px;line-height:46px;color:#333}
.nav li.active{background:var(--red);color:var(--white);padding:0 18px;margin-right:8px}

/* hero */
.hero{height:566px;background:linear-gradient(120deg,#6b6b6b 0%,#cfcfcf 35%,#f4f4f4 55%,#bdbdbd 80%,#7a7a7a 100%)}

/* services */
.services{height:364px;background:var(--light)}
.service{position:absolute;top:50px;width:300px;text-align:center}
.service svg{width:70px;height:70px}
.service h3{font-weight:400;font-size:18px;margin-top:18px;color:#222}
.service p{font-size:14px;line-height:22px;color:var(--muted);margin-top:10px}

/* welcome */
.welcome{height:383px;text-align:center}
.welcome h2{padding-top:58px}
.welcome p{width:920px;margin:18px auto 0;font-size:14px;line-height:23px;color:var(--muted)}
.welcome .btn{margin-top:22px;width:166px;height:57px;line-height:57px}

/* testimonial */
.testimonial{height:311px;background:radial-gradient(ellipse at 75% 70%,#3a302a 0%,#1a1a1a 45%,#0d0d0d 100%);color:var(--white);text-align:center}
.testimonial h2{padding-top:60px;color:var(--white)}
.testimonial blockquote{width:820px;margin:26px auto 0;font-size:15px;line-height:26px;color:#ddd}
.testimonial cite{display:block;margin-top:14px;color:var(--red);font-style:normal;font-size:14px}
.quote-mark{position:absolute;top:110px;font-family:Georgia,serif;font-size:130px;color:#555;line-height:1}

/* band */
.band{height:128px;background:var(--red);color:var(--white)}
.band p{position:absolute;left:80px;top:28px;width:760px;font-size:24px;line-height:34px}
.band .btn-white{position:absolute;right:78px;top:34px;width:240px;height:57px;line-height:57px;background:var(--white);color:var(--red);text-align:center;font-size:19px;border-radius:4px}

/* attorney */
.attorney{height:332px}
.attorney .photo{position:absolute;left:0;top:62px;width:185px;height:206px;border:3px solid var(--red);background:linear-gradient(160deg,#4a3226,#b48a72 55%,#e0c3ad)}
.attorney h2{position:absolute;left:210px;top:50px;text-align:left}
.attorney .role{position:absolute;left:210px;top:110px;color:var(--red);font-style:italic;font-size:17px}
.attorney p{position:absolute;left:210px;top:145px;width:834px;font-size:14px;line-height:23px;color:var(--muted)}

/* contact */
.contact{height:446px;background:radial-gradient(ellipse at 80% 80%,#3b2f26 0%,#171717 50%,#0c0c0c 100%)}
.contact h2{padding-top:56px;color:var(--white)}
.form{position:absolute;left:202px;top:128px;width:798px}
.field{position:absolute;height:52px;border:1px solid #666;background:rgba(0,0,0,.25);color:#ddd;font-size:14px;padding:12px 10px}
.submit{position:absolute;left:316px;top:200px;width:166px;height:57px;line-height:57px}

/* blog */
.blog{height:451px}
.blog h2{padding-top:42px}
.post{position:absolute;top:140px;width:515px;height:251px;background:#f2f2f2}
.post .thumb{position:absolute;left:0;top:0;width:208px;height:251px}
.post .date{position:absolute;left:228px;top:0;width:80px;height:92px;background:var(--red);color:var(--white);text-align:center;font-size:26px;line-height:30px;padding-top:12px}
.post .date em{display:block;font-size:24px}
.post h3{position:absolute;left:228px;top:106px;font-weight:400;font-size:18px}
.post p{position:absolute;left:228px;top:140px;width:260px;font-size:14px;line-height:22px;color:var(--muted)}

/* badges */
.badges{height:178px;background:var(--light)}

/* footer */
.footer{height:225px;background:var(--black);color:var(--white)}
.footer-nav{position:absolute;left:80px;top:42px;display:flex;gap:36px;font-size:15px;list-style:none}
.social{position:absolute;top:30px;width:46px;height:46px;border-radius:50%}
.social.filled{background:var(--red)}
.social.ring{border:2px solid var(--red)}
.divider{position:absolute;left:78px;right:78px;top:102px;border-top:1px solid #333}
.info{position:absolute;top:134px;display:flex;align-items:center;gap:14px;font-size:14px;line-height:22px}
.info .ico{width:46px;height:46px;border-radius:50%;display:flex;align-items:center;justify-content:center}
.info .ico.solid{background:var(--red)}
.info .ico.outline{border:2px solid var(--red)}
.copyright{height:63px;background:var(--red);color:var(--white);text-align:center;font-size:14px;line-height:63px}
</style>
</head>
<body>

<header class="section header">
  <div class="logo"><div class="name">Tidecrest Law</div><div class="sub">P.C.</div></div>
  <ul class="nav">
    <li class="active">HOME</li><li>ATTORNEY PROFILE</li><li>PRACTICE AREA</li><li>CLIENT REVIEWS</li><li>LINKS</li><li>CONTACT US</li>
  </ul>
</header>

<section class="section hero" role="img" aria-label="Word cloud of legal terms centred on the words criminal law over a photo of a desk with a gavel"></section>

<section class="section services">
  <div class="service" style="left:122px">
    <svg viewBox="0 0 70 70" fill="none" stroke="#ec1f27" stroke-width="3"><rect x="10" y="22" width="50" height="34" rx="3"/><path d="M26 22v-7h18v7M10 36h50M31 36v6h8v-6"/></svg>
    <h3>BUSINESS LAW</h3>
    <p>Small &amp; medium-sized businesses have many of the same legal issues that affect large businesses, such as business structure..</p>
  </div>
  <div class="service" style="left:450px">
    <svg viewBox="0 0 70 70" fill="none" stroke="#ec1f27" stroke-width="3"><path d="M8 34L35 10l27 24M16 28v30h38V28"/><path d="M28 46l10-10M33 33l8 8M26 52h14"/></svg>
    <h3>REAL ESTATE LAW</h3>
    <p>At Tidecrest Law P.C., we help Californians who need legal advice and representation for Real Estate Law activities, such as..</p>
  </div>
  <div class="service" style="left:835px">
    <svg viewBox="0 0 70 70" fill="none" stroke="#ec1f27" stroke-width="3"><circle cx="35" cy="24" r="15"/><path d="M40 18h-7a4 4 0 0 0 0 8h4a4 4 0 0 1 0 8h-8M35 14v4M35 34v4M12 40l14 14 10-8 20 14"/><path d="M50 60h7v-7"/></svg>
    <h3>BANKRUPTCY LAW</h3>
    <p>If your finances are dwindling to the point where you can no longer pay your bills, and you are getting harassed by..</p>
  </div>
</section>

<section class="section welcome">
  <h2>WELCOME TO <span class="accent">TIDECREST LAW P.C</span></h2>
  <p>Tidecrest Law P.C. is owned by Renata K. Vale, a dedicated and caring professional who uses her broad range of skills as a California lawyer to bring consumers and business owners exceptionally strong legal representation that achieves best results.<br>She works with people from across the northern region of California, from the Northern border to the Central Valley region. They bring her legal concerns and problems that occur in many areas of law, including Real Estate, Family law, Business Law, Bankruptcy, Criminal Law and Civil Litigation.</p>
  <span class="btn">KNOW MORE</span>
</section>

<section class="section testimonial">
  <span class="quote-mark" style="left:140px">&ldquo;</span>
  <span class="quote-mark" style="right:140px;top:150px">&rdquo;</span>
  <h2>WHAT OUR <span class="accent">CLIENT SAY</span></h2>
  <blockquote>Tidecrest Law has met and exceeded our expectations in assisting our company with our real estate legal needs. In an area of law where the rules our ever changing, we simply could not navigate our company effectively without their help.
    <cite>&mdash; Halden Commercial</cite>
  </blockquote>
</section>

<section class="section band">
  <p>Tidecrest Law, P.C. provides experienced, compassionate legal guidance and representation to businesses.</p>
  <span class="btn-white">TALLYDOCK ACCOUNT</span>
</section>

<section class="section attorney">
  <div class="wrap">
    <div class="photo" role="img" aria-label="Portrait photo of the attorney"></div>
    <h2>OUR <span class="accent">ATTORNEY</span></h2>
    <div class="role">Renata K. Vale, Esq.</div>
    <p>People from the north state region of California, from the Central Valley to the Northern border, look to Tidecrest Law, P.C., in Redding, CA, for experienced legal services offered by Attorney Renata K. Vale. Renata is a friendly, dedicated lawyer who is skilled in the law practice areas of Business Law, Real Estate, Bankruptcy, Family Law, Criminal Law and Civil Litigation. These legal services are needed by consumers and business owners alike, especially people who want top quality legal representation from a caring attorney ..</p>
  </div>
</section>

<section class="section contact" role="group" aria-label="Contact form over a dark photo of scales and a gavel">
  <h2>CONTACT <span class="accent">US</span></h2>
  <div class="form">
    <div class="field" style="left:0;top:0;width:258px">Name*</div>
    <div class="field" style="left:270px;top:0;width:258px">Email*</div>
    <div class="field" style="left:540px;top:0;width:258px">Phone*</div>
    <div class="field" style="left:0;top:64px;width:798px;height:123px">Message*</div>
    <span class="btn submit">SUBMIT</span>
  </div>
</section>

<section class="section blog">
  <h2>LATEST <span class="accent">BLOG</span></h2>
  <article class="post" style="left:78px">
    <div class="thumb" role="img" aria-label="Photo of a Lady Justice statue against the sky" style="background:linear-gradient(180deg,#c7d3dc,#6d7378 70%,#3a3d40)"></div>
    <div class="date">Aug<em>03</em></div>
    <h3>LOREM IPSUM IS SIMPLE</h3>
    <p>Lorem Ipsum is simply dummy text of the print ing and typesetting industry. Lorem Ipsum has been the industry's standard..</p>
  </article>
  <article class="post" style="left:607px">
    <div class="thumb" role="img" aria-label="Photo of scales of justice in blue light" style="background:linear-gradient(180deg,#1d2a3a,#7f93ad 50%,#2a3446)"></div>
    <div class="date">Aug<em>03</em></div>
    <h3>LOREM IPSUM IS SIMPLE</h3>
    <p>Lorem Ipsum is simply dummy text of the print ing and typesetting industry. Lorem Ipsum has been the industry's standard..</p>
  </article>
</section>

<section class="section badges">
  <svg width="1200" height="178" aria-label="Partner and listing badges">
    <circle cx="391" cy="89" r="58" fill="#2f6fb3"/>
    <rect x="472" y="62" width="282" height="56" rx="4" fill="#c9ced6"/>
    <circle cx="830" cy="89" r="58" fill="none" stroke="#555" stroke-width="4"/>
  </svg>
</section>

<footer class="section footer">
  <ul class="footer-nav"><li>Home</li><li>Attorney Profile</li><li>Practice Areas</li><li>Client Reviews</li><li>Links</li><li>Contact Us</li></ul>
  <span class="social filled" style="left:949px"></span>
  <span class="social ring" style="left:1013px"></span>
  <span class="social ring" style="left:1075px"></span>
  <div class="divider"></div>
  <div class="info" style="left:78px">
    <span class="ico solid"><svg width="20" height="24" viewBox="0 0 20 24"><path d="M10 0a8 8 0 0 0-8 8c0 6 8 16 8 16s8-10 8-16a8 8 0 0 0-8-8z" fill="#fff"/><circle cx="10" cy="8" r="3" fill="#ec1f27"/></svg></span>
    <span>Tidecrest Law, P.C. Office 125<br>418 Harbor Lane Suite 200<br>Redding, CA 96001</span>
  </div>
  <div class="info" style="left:345px">
    <span class="ico outline"><svg width="20" height="20" viewBox="0 0 20 20"><path d="M4 1l4 4-2 3a11 11 0 0 0 6 6l3-2 4 4-3 3C8 19 1 12 1 4z" fill="#ec1f27"/></svg></span>
    <span>(555) 014-2280</span>
  </div>
  <div class="info" style="left:610px">
    <span class="ico outline"><svg width="20" height="20" viewBox="0 0 20 20"><rect x="2" y="6" width="16" height="12" rx="2" fill="#ec1f27"/><rect x="6" y="2" width="8" height="5" fill="none" stroke="#ec1f27" stroke-width="2"/></svg></span>
    <span>(555) 019-3371</span>
  </div>
  <div class="info" style="left:848px">
    <span class="ico outline"><svg width="20" height="16" viewBox="0 0 20 16"><rect x="1" y="1" width="18" height="14" rx="2" fill="#ec1f27"/><path d="M1 2l9 7 9-7" fill="none" stroke="#000" stroke-width="1.5"/></svg></span>
    <span>renata@tidecrestlaw.com</span>
  </div>
</footer>

<div class="section copyright">&copy; Tidecrest Law, P.C. 2016. All rights reserved.</div>

</body>
</html>
```